Dravel

We are openıng one huntıng showroom in Riyadh? Saudi Arabia. Company name is "DRAVEL".
Our logo designed and we need Business Card Design now.
I attached DRAVEL logo below.
Front side will English and back side will be Arabic

```html
<!DOCTYPE html>
<html lang="en">
<head>
<meta charset="utf-8">
<title>Dravel Business Card</title>
<link href="https://fonts.googleapis.com/css2?family=Cairo:wght@700&family=Lato:wght@400;700;900&display=swap" rel="stylesheet">
<style>
  :root {
    --stage: #e4e5e4;
    --card-white: #fcf8f7;
    --green-dark: #0a7a43;
    --green-back: #0b8448;
    --green-back-soft: #17905a;
    --green-olive: #6f9e35;
    --ink: #1c1c1c;
    --rule: #d8d4d2;
    --white: #ffffff;
  }
  html, body {
    margin: 0;
    padding: 0;
    width: 1200px;
    height: 782px;
    overflow: hidden;
    background: var(--stage);
    font-family: "Lato", sans-serif;
  }
  .canvas {
    position: relative;
    width: 1200px;
    height: 782px;
  }
  .card {
    position: absolute;
    top: 241px;
    width: 520px;
    height: 300px;
    box-shadow: 0 6px 18px rgba(0,0,0,0.18);
    overflow: hidden;
  }
  .card-front { left: 60px; background: var(--card-white); }
  .card-back  { left: 620px; background: var(--green-back); }

  .back-texture {
    position: absolute;
    inset: 0;
    background: linear-gradient(135deg, var(--green-back-soft) 0%, var(--green-back) 55%, var(--green-back-soft) 100%);
  }

  .brand-name {
    position: absolute;
    font-family: "Lato", sans-serif;
    font-weight: 900;
    letter-spacing: 1px;
    margin: 0;
    line-height: 1;
  }
  .card-front .brand-name {
    left: 34px;
    top: 88px;
    font-size: 52px;
    color: var(--green-dark);
  }

  .back-brand {
    position: absolute;
    right: 48px;
    top: 168px;
    margin: 0;
    text-align: right;
    color: var(--white);
  }
  .back-brand .brand-name {
    position: static;
    display: block;
    font-size: 34px;
  }
  .brand-name-arabic {
    display: block;
    font-family: "Cairo", sans-serif;
    font-weight: 700;
    font-size: 28px;
    line-height: 1.3;
    margin-top: 4px;
    direction: rtl;
  }

  .divider {
    position: absolute;
    left: 262px;
    top: 70px;
    width: 1px;
    height: 160px;
    background: var(--rule);
  }

  .contact {
    position: absolute;
    left: 280px;
    top: 72px;
    color: var(--ink);
  }
  .contact-name {
    margin: 0;
    font-size: 21px;
    font-weight: 400;
    letter-spacing: 1px;
    color: var(--green-dark);
    line-height: 1;
  }
  .contact-title {
    margin: 3px 0 8px;
    font-size: 14px;
  }
  .contact-list {
    list-style: none;
    margin: 0;
    padding: 0;
    font-size: 14px;
    line-height: 19px;
  }
  .contact-list li {
    display: flex;
    align-items: center;
    gap: 6px;
  }
  .contact-list svg { width: 10px; height: 10px; flex: none; fill: var(--green-dark); }
  .address {
    margin: 2px 0 0;
    font-size: 14px;
    line-height: 18px;
  }

  .bottom-bands {
    position: absolute;
    left: 0;
    bottom: 0;
    width: 520px;
    height: 46px;
  }
</style>
</head>
<body>
<main class="canvas">
  <section class="card card-front" aria-label="Business card, English side">
    <h1 class="brand-name">DRAVEL</h1>
    <div class="divider"></div>
    <div class="contact">
      <h2 class="contact-name">OMAR HADDAD</h2>
      <p class="contact-title">Managing Director</p>
      <ul class="contact-list">
        <li>
          <svg viewBox="0 0 10 10" aria-hidden="true"><path d="M1 2c0-1 1-1.5 2-1.5l1 2-1 1c.5 1.2 1.3 2 2.5 2.5l1-1 2 1c0 1-.5 2-1.5 2C3.5 8 1 5.5 1 2z"/></svg>
          011-482 730 615
        </li>
        <li>
          <svg viewBox="0 0 10 10" aria-hidden="true"><path d="M0 2h10v6H0z"/><path d="M0 2l5 3.5L10 2" stroke="#fcf8f7" fill="none"/></svg>
          info@dravelhunt.com
        </li>
        <li>
          <svg viewBox="0 0 10 10" aria-hidden="true"><circle cx="5" cy="5" r="4.6"/></svg>
          www.dravelhunt.com
        </li>
      </ul>
      <p class="address">17, King Fahd Road<br>Riyadh, 11564</p>
    </div>
    <svg class="bottom-bands" viewBox="0 0 520 46" aria-hidden="true">
      <polygon points="0,4 312,4 300,46 0,46" fill="var(--green-dark)"/>
      <polygon points="318,18 520,18 520,40 310,40" fill="var(--green-olive)"/>
    </svg>
  </section>

  <section class="card card-back" aria-label="Business card, Arabic side">
    <div class="back-texture" role="img" aria-label="Repeating brand pattern in soft green tones"></div>
    <h2 class="back-brand">
      <span class="brand-name">DRAVEL</span>
      <span class="brand-name-arabic" lang="ar">درافل</span>
    </h2>
  </section>
</main>
</body>
</html>
```